Lantern Advisory Business Cards

We need a new layout for our business cards. We have a logo already. But we might be interested in only using the Lantern portion of the logo. It has been uploaded.

We would like cards that are not overly busy. Clean. Modern. Perhaps a gray color for one side.

On the back, we would like to have the lantern part of the logo and "Step forward, we stand by you!"

Our business provides medics and safety training for corporate clients. Our website is www.lanternadvisoryllc.example.

Industry/Entity Type

Business

Contact Information for Business Card

We want include name, email address, cell phone, main line number, and website URL on the front. Use the following as an example: Marla Tobin, marla@lanternadvisoryllc.example, 402.318.7264 (cell), 402.947.315, and www.lanternadvisoryllc.example.

Font styles to use
Serif
Sans Serif

Requirements
Must have
• All required information. Back side logo with "Take the leap, we will catch you!"
Nice to have
• If possible, we would like to consider creating a card in a non-standard shape. Perhaps, the shape of a lantern. Just interested in understanding the option.

```html
<!DOCTYPE html>
<html lang="en">
<head>
<meta charset="utf-8">
<title>Lantern Advisory Business Cards</title>
<link rel="stylesheet" href="https://fonts.googleapis.com/css2?family=Cinzel:wght@400;500&family=Montserrat:wght@400;600&display=swap">
<style>
  :root {
    --backdrop: #2b2b2d;
    --card: #070707;
    --ink: #f2f2f2;
    --accent: #1f5fae;
    --accent-bright: #2e7fd9;
    --rule: #8a8a8a;
  }
  * { box-sizing: border-box; margin: 0; padding: 0; }
  html, body { width: 1200px; height: 900px; overflow: hidden; }
  body {
    background: var(--backdrop);
    position: relative;
    font-family: "Montserrat", sans-serif;
    color: var(--ink);
  }
  .card {
    position: absolute;
    width: 580px;
    height: 330px;
    background: var(--card);
    border-radius: 22px;
    box-shadow: 0 18px 40px rgba(0,0,0,0.55);
  }
  .card--brand { left: 70px; top: 80px; }
  .card--contact { left: 550px; top: 490px; }

  /* brand side */
  .brand {
    position: absolute;
    left: 0; right: 0; top: 96px;
    text-align: center;
  }
  .brand__mark {
    display: inline-flex;
    align-items: center;
    gap: 12px;
  }
  .brand__dot {
    width: 16px; height: 16px;
    border-radius: 50%;
    background: var(--accent);
  }
  .brand__name {
    font-family: "Montserrat", sans-serif;
    font-weight: 400;
    font-size: 30px;
    letter-spacing: 0.5px;
    color: var(--ink);
  }
  .brand__tagline {
    margin-top: 10px;
    font-size: 10px;
    letter-spacing: 4px;
    text-transform: uppercase;
    color: var(--ink);
  }
  .brand__slogan {
    position: absolute;
    left: 0; right: 0; bottom: 72px;
    text-align: center;
    font-weight: 600;
    font-size: 16px;
    letter-spacing: 0.8px;
    text-transform: uppercase;
  }

  /* contact side */
  .contact__logo {
    position: absolute;
    left: 0; width: 250px; top: 0; bottom: 0;
    display: flex; align-items: center; justify-content: center;
  }
  .contact__logo-name {
    font-family: "Montserrat", sans-serif;
    font-weight: 400;
    font-size: 28px;
    color: var(--accent);
  }
  .contact__divider {
    position: absolute;
    left: 250px; top: 90px;
    width: 1px; height: 150px;
    background: linear-gradient(to bottom, transparent, var(--rule), transparent);
  }
  .contact__details {
    position: absolute;
    left: 285px; top: 92px;
  }
  .contact__name {
    font-family: "Cinzel", serif;
    font-weight: 500;
    font-size: 24px;
    color: var(--accent);
    letter-spacing: 1px;
    margin-bottom: 10px;
  }
  .contact__list { list-style: none; }
  .contact__item {
    display: flex; align-items: center; gap: 10px;
    font-size: 14px;
    line-height: 24px;
  }
  .contact__item svg { width: 12px; height: 12px; flex: none; }
  .contact__web { color: var(--accent-bright); }
</style>
</head>
<body>

<section class="card card--brand">
  <div class="brand">
    <div class="brand__mark">
      <span class="brand__dot"></span>
      <span class="brand__name">Lantern Advisory</span>
    </div>
    <p class="brand__tagline">The Ready Response Team</p>
  </div>
  <p class="brand__slogan">Step forward, we stand by you</p>
</section>

<section class="card card--contact">
  <div class="contact__logo">
    <span class="contact__logo-name">Lantern</span>
  </div>
  <div class="contact__divider"></div>
  <div class="contact__details">
    <h1 class="contact__name">Marla Tobin</h1>
    <ul class="contact__list">
      <li class="contact__item">
        <svg viewBox="0 0 12 12"><rect x="3" y="0.5" width="6" height="11" rx="1.2" fill="none" stroke="#1f5fae" stroke-width="1.2"/><circle cx="6" cy="9.5" r="0.7" fill="#1f5fae"/></svg>
        <span>402.318.7264</span>
      </li>
      <li class="contact__item">
        <svg viewBox="0 0 12 12"><path d="M2.5 1 L4.5 1 L5.3 3.5 L4 4.6 Q5 7 7.4 8 L8.5 6.7 L11 7.5 L11 9.5 Q10.5 11 9 11 Q1 10 1 2.8 Q1 1.2 2.5 1 Z" fill="#1f5fae"/></svg>
        <span>402.947.315(main)</span>
      </li>
      <li class="contact__item">
        <svg viewBox="0 0 12 12"><rect x="0.6" y="2.2" width="10.8" height="7.6" fill="none" stroke="#1f5fae" stroke-width="1.2"/><path d="M0.8 2.6 L6 6.6 L11.2 2.6" fill="none" stroke="#1f5fae" stroke-width="1.2"/></svg>
        <span>marla@lanternadvisoryllc.example</span>
      </li>
      <li class="contact__item">
        <svg viewBox="0 0 12 12"><circle cx="6" cy="6" r="5.3" fill="#1f5fae"/><path d="M0.8 6 H11.2 M6 0.8 Q3 6 6 11.2 M6 0.8 Q9 6 6 11.2" fill="none" stroke="#070707" stroke-width="0.8"/></svg>
        <span>www.<span class="contact__web">lanternadvisoryllc.example</span></span>
      </li>
    </ul>
  </div>
</section>

</body>
</html>
```